We need a home page that represents us as the best Veterinary Hospital in the State

We need webdesign for a Vet Hospital in Rio de Janeiro, Brazil.
We think the current design is very childish. We want something that looks more like a hospital and not a clinic.
We put a map to guide the content of the sections and also an example of a layout that we don't like but that may serve as a reference as a wireframe.

Target Market(s)

pet owners

Industry/Entity Type

Pet Care

Number of Pages Required

1 page

Requirements
Must have
• Here is a map of the sections and texts we think for home: https://qx.vz/5719382046?t=PlorvKanbe
Nice to have
• some sites we like:
https://www.valtorim.br/Pages/Home.aspx
https://www.pelmarvito.com/
Should not have
• This is a design that we started working on and the content is correct. But the layout is poor in detail, bad colors, CTA's without prominence.

https://ronalbekwistudio.plotvarex.com/console/share/KT7N9H2WRM/918273645

```html
<!DOCTYPE html>
<html lang="en">
<head>
<meta charset="utf-8">
<title>Vita Pet 24h – Veterinary Hospital</title>
<link href="https://fonts.googleapis.com/css2?family=Signika:wght@300;400;500;600&family=Arimo:wght@400;700&display=swap" rel="stylesheet">
<style>
:root{
  --blue:#0e56a6;
  --red:#b5082d;
  --ink:#333;
  --muted:#555;
  --hero:#efeff1;
  --line:#dcdcdc;
  --white:#fff;
}
*{margin:0;padding:0;box-sizing:border-box}
html,body{width:1200px;height:3967px;overflow:hidden}
body{position:relative;background:var(--white);font-family:"Signika",sans-serif;color:var(--ink)}
.abs{position:absolute}
a{color:inherit;text-decoration:none}

/* header */
.header{top:0;left:0;width:1200px;height:140px;background:var(--white)}
.brand{left:111px;top:44px;display:flex;align-items:center;gap:14px}
.brand-mark{width:40px;height:40px;border-radius:50%;background:var(--red)}
.brand-name{font-size:44px;font-weight:600;color:var(--blue)}
.search{left:801px;top:51px;width:286px;height:49px;border:1px solid #cfcfcf;border-radius:3px;font-size:15px;color:#555;padding:15px 13px;font-family:"Arimo",sans-serif}
.search svg{position:absolute;right:16px;top:16px}

.nav{top:140px;left:0;width:1200px;height:65px;background:var(--blue)}
.nav ul{list-style:none;display:flex;position:absolute;left:137px;top:0;height:65px;align-items:center;gap:0}
.nav li{color:#fff;font-size:12.5px;font-weight:500;letter-spacing:.2px;margin-right:35px}

/* hero */
.hero{top:205px;left:0;width:1200px;height:685px;background:var(--hero);overflow:hidden}
.hero-shape{left:-230px;top:-150px;width:690px;height:690px;border-radius:50%;background:#e4e4e6}
.hero h1{left:111px;top:178px;width:500px;font-size:40px;line-height:54px;font-weight:600;color:var(--blue)}
.hero h1 em{font-style:normal;color:var(--red)}
.hero p{left:111px;top:363px;width:480px;font-size:21px;line-height:34px;color:#333;font-weight:400}
.btn{display:inline-block;border-radius:30px;color:#fff;font-weight:600;text-align:center}
.hero .btn{left:111px;top:462px;width:205px;height:58px;line-height:58px;background:var(--blue);font-size:18px}
.photo-circle{border-radius:50%;border:6px solid #fff;overflow:hidden;box-shadow:0 2px 8px rgba(0,0,0,.12)}
.photo-big{left:675px;top:80px;width:446px;height:446px;background:radial-gradient(circle at 55% 55%,#d8b070,#8a6a3a 55%,#3c5a2a)}
.photo-small{left:613px;top:357px;width:284px;height:284px;background:radial-gradient(circle at 50% 40%,#9aa3ad,#6b7078 60%,#cfc6bd)}
.tag{position:absolute;left:0;width:100%;color:#fff;font-size:16px;text-align:center}
.photo-big .tag{top:326px;height:68px;line-height:68px;background:var(--red);padding-left:180px}
.photo-small .tag{top:208px;height:58px;line-height:58px;background:var(--blue)}

/* services */
.services{top:890px;left:0;width:1200px;height:193px;display:flex}
.service{flex:1;display:flex;flex-direction:column;align-items:center;color:#fff;border-right:2px solid rgba(255,255,255,.2)}
.service:nth-child(odd){background:var(--blue)}
.service:nth-child(even){background:var(--red)}
.service svg{margin-top:38px;height:62px}
.service span{margin-top:22px;font-size:23px;font-weight:500;letter-spacing:.3px}

/* section titles */
.section-title{left:0;width:1200px;text-align:center;color:var(--blue);font-size:44px;font-weight:500}
.rule{height:3px;width:52px;background:var(--blue)}

/* unit cards */
.unit{top:1241px;width:310px;height:441px;border:1px solid var(--line);border-radius:5px;background:#fff;box-shadow:0 1px 4px rgba(0,0,0,.08);overflow:hidden;text-align:center}
.unit-photo{height:228px}
.unit h3{margin-top:26px;font-size:26px;font-weight:400;color:#333}
.unit p{margin-top:12px;font-family:"Arimo",sans-serif;font-size:13.5px;line-height:25px;color:#555;padding:0 18px}
.unit .btn{margin-top:18px;width:145px;height:50px;line-height:50px;font-size:15px;font-weight:500}

/* infrastructure */
.infra{top:1779px;left:0;width:1200px;height:443px;background:var(--blue)}
.infra h2{position:absolute;left:0;top:32px;width:1200px;text-align:center;color:#fff;font-size:35px;font-weight:400;line-height:48px}
.infra p{position:absolute;left:0;top:150px;width:1200px;text-align:center;color:#fff;font-size:23px;font-weight:300}
.video{left:188px;top:2010px;width:823px;height:451px;border:3px solid #fff;background:linear-gradient(100deg,#6f7a86,#3e5f92 45%,#8ca0b8);box-shadow:0 2px 8px rgba(0,0,0,.15)}
.play{position:absolute;left:358px;top:173px;width:100px;height:100px;border-radius:50%;background:rgba(30,30,30,.75);border:3px solid rgba(255,255,255,.7)}

/* testimonial */
.testimonial-photo{left:0;top:2461px;width:600px;height:550px;background:linear-gradient(90deg,#f3ece6 0%,#d9a070 25%,#c88a5a 45%,#f7f2ee 80%,#fff 100%)}
.testimonial h2{left:550px;top:2580px;font-size:46px;font-weight:400;color:var(--blue)}
.testimonial .rule{left:554px;top:2657px;width:76px}
.quote{left:556px;top:2690px;width:494px;font-family:"Arimo",sans-serif;font-size:13.2px;line-height:29.3px;color:#444}
.author{left:556px;top:2888px;font-size:22px;color:var(--blue)}

/* blog */
.post{top:3168px;width:468px;height:362px;border:1px solid var(--line);background:#fff}
.post-photo{position:relative;height:220px}
.post-date{position:absolute;left:0;bottom:0;width:155px;height:40px;line-height:40px;background:var(--red);color:#fff;font-size:14px;padding-left:17px;clip-path:polygon(0 0,84% 0,100% 100%,0 100%)}
.post h3{margin:38px 22px 0;font-size:19px;font-weight:400;color:#333}
.post p{margin:10px 22px 0;font-family:"Arimo",sans-serif;font-size:13px;line-height:26px;color:#666}
.post p b{color:var(--blue)}

/* footer */
.footer{top:3604px;left:0;width:1200px;height:363px;background:var(--blue);color:#fff}
.col{position:absolute;top:46px}
.col h4{font-size:32px;font-weight:400;margin-bottom:10px}
.col li{list-style:none;font-size:14px;line-height:29.5px;font-weight:300}
.footer-rule{position:absolute;left:112px;top:277px;width:976px;height:1px;background:rgba(255,255,255,.25)}
.social{position:absolute;top:300px;left:111px;display:flex;gap:8px}
.social span{width:36px;height:36px;border:2px solid #fff;border-radius:50%}
.copyright{position:absolute;right:112px;top:313px;font-size:12.5px;font-weight:300}
</style>
</head>
<body>

<header class="abs header">
  <div class="abs brand"><span class="brand-mark"></span><span class="brand-name">Vita Pet</span></div>
  <div class="abs search">SEARCH
    <svg width="14" height="14" viewBox="0 0 14 14"><circle cx="6" cy="6" r="4.5" fill="none" stroke="#444" stroke-width="1.8"/><line x1="9.3" y1="9.3" x2="13" y2="13" stroke="#444" stroke-width="1.8"/></svg>
  </div>
</header>

<nav class="abs nav">
  <ul>
    <li>HOME</li><li>UNITS</li><li>SCHEDULES</li><li>SPECIALTIES</li><li>BLOG</li><li>VACCINES</li><li>WORK WITH US</li><li>THE VITA PET</li><li>TUTOR AREA</li><li>TEAM</li>
  </ul>
</nav>

<section class="abs hero">
  <div class="abs hero-shape"></div>
  <h1 class="abs">Dedication <em>24 hours a day 7 days a week</em> to take care of those you love!</h1>
  <p class="abs">Excellent doctors and complete infrastructure at a price that fits in your pocket</p>
  <a class="abs btn">Emergency Room</a>
  <div class="abs photo-circle photo-big" role="img" aria-label="Smiling golden retriever outdoors"><div class="tag">FLORA</div></div>
  <div class="abs photo-circle photo-small" role="img" aria-label="Grey cat being petted under the chin"><div class="tag">NUVEM</div></div>
</section>

<section class="abs services">
  <div class="service">
    <svg viewBox="0 0 60 60" width="62" fill="none" stroke="#fff" stroke-width="2.4"><path d="M6 30 30 8l24 22"/><path d="M11 26v28h38V26"/><path d="M24 54V40h12v14"/><path d="M30 16v10M25 21h10"/></svg>
    <span>Pronto-Socorro</span>
  </div>
  <div class="service">
    <svg viewBox="0 0 60 60" width="62" fill="none" stroke="#fff" stroke-width="2.4"><rect x="6" y="12" width="48" height="32" rx="2"/><rect x="18" y="20" width="14" height="30" rx="2"/><path d="M38 44v8M30 52h18"/></svg>
    <span>Consultas</span>
  </div>
  <div class="service">
    <svg viewBox="0 0 60 60" width="62" fill="none" stroke="#fff" stroke-width="2.4"><rect x="6" y="12" width="48" height="42" rx="3"/><path d="M6 24h48M18 6v12M42 6v12M22 38l6 6 12-12"/></svg>
    <span>Agendamentos</span>
  </div>
  <div class="service">
    <svg viewBox="0 0 60 60" width="62" fill="none" stroke="#fff" stroke-width="2.4"><path d="M44 4l12 12M50 10l-8 8M40 12l8 8-26 26-8-8z"/><path d="M14 38l-8 8M6 46l-2 10 10-2M26 24l4 4M22 28l4 4M18 32l4 4"/></svg>
    <span>Vacinas</span>
  </div>
  <div class="service">
    <svg viewBox="0 0 60 60" width="62" fill="none" stroke="#fff" stroke-width="2.4"><path d="M12 4h26l12 12v40H12z"/><path d="M38 4v12h12M31 14v12M25 20h12M20 36h22M20 43h22M20 50h22"/></svg>
    <span>Resultados</span>
  </div>
</section>

<h2 class="abs section-title" style="top:1138px">Vita Pet Units</h2>
<div class="abs rule" style="left:574px;top:1204px"></div>

<article class="abs unit" style="left:111px">
  <div class="unit-photo" role="img" aria-label="Veterinarian smiling with a labrador" style="background:linear-gradient(120deg,#e8ecef,#d9c39a 60%,#cfa866)"></div>
  <h3>Taquara - RJ</h3>
  <p>Rua Alvares Lemos, 318 - Copacabana,<br>Rio de Janeiro - RJ, 22041-110</p>
  <a class="btn" style="background:var(--blue)">Veja no mapa</a>
</article>
<article class="abs unit" style="left:445px">
  <div class="unit-photo" role="img" aria-label="Fluffy cat resting on a vet's shoulder" style="background:linear-gradient(120deg,#dfe3e8,#9ea2a8 55%,#6b8fc4)"></div>
  <h3>Flamengo - RJ</h3>
  <p>Rua Alvares Lemos, 318 - Copacabana,<br>Rio de Janeiro - RJ, 22041-110</p>
  <a class="btn" style="background:var(--red)">Veja no mapa</a>
</article>
<article class="abs unit" style="left:778px">
  <div class="unit-photo" role="img" aria-label="Vet examining a dog in the clinic" style="background:linear-gradient(120deg,#6fa4a8,#c9b08a 55%,#e2d6c2)"></div>
  <h3>Copacabana - RJ</h3>
  <p>Rua Alvares Lemos, 318 - Copacabana,<br>Rio de Janeiro - RJ, 22041-110</p>
  <a class="btn" style="background:var(--blue)">Veja no mapa</a>
</article>

<section class="abs infra">
  <h2>Complete infrastructure &amp;<br>medical staff available 24 hours a day</h2>
  <p>Emergency room, detention center, imaging exams. surgery.</p>
</section>
<div class="abs video" role="img" aria-label="Video: two smiling veterinarians holding a small dog">
  <div class="play"><svg width="100" height="100" viewBox="0 0 100 100" style="position:absolute;left:-3px;top:-3px"><path d="M40 31l30 19-30 19z" fill="#fff"/></svg></div>
</div>

<div class="abs testimonial-photo" role="img" aria-label="Dog raising its paw"></div>
<div class="testimonial">
  <h2 class="abs">What Some Tutors Say</h2>
  <div class="abs rule"></div>
  <p class="abs quote">Sed ut perspiciatis unde omnis iste natus error sit voluptatem accusantium dol oremque laudantium, totam rem aperiam, eaque ipsa quae ab illo inventore verit atis et quasi architecto beatae vitae dicta sunt explicabo. Nemo enim ipsam volupt atem quia voluptas sit aspernatur aut odit aut fugit, sed quia consequuntur magni dolores eos qui ratione voluptatem sequi nesciunt. Neque porro quisquam est, qui dolorem ipsum quia dolor sit amet, consectetur, adipisci velit,</p>
  <p class="abs author">-Lia Fontes</p>
</div>

<h2 class="abs section-title" style="top:3052px">Latest Blog Article</h2>
<div class="abs rule" style="left:574px;top:3121px"></div>

<article class="abs post" style="left:112px">
  <div class="post-photo" role="img" aria-label="Vet smiling with a beagle" style="background:linear-gradient(110deg,#3f6fb0,#c89a7a 45%,#e8e2da)"><div class="post-date">02 MARCH 2021</div></div>
  <h3>SED UT PERSPICIATIS UNDE OMNIS</h3>
  <p>Nemo enim ipsam voluptatem quia voluptas sit aspernatur aut odit aut qui ratione voluptatem sequi nesciunt. <b>READ MORE</b></p>
</article>
<article class="abs post" style="left:621px">
  <div class="post-photo" role="img" aria-label="Vet holding a tabby cat" style="background:linear-gradient(110deg,#2f66b4,#6d8fc0 45%,#b9aa96)"><div class="post-date">02 MARCH 2021</div></div>
  <h3>SED UT PERSPICIATIS UNDE OMNIS</h3>
  <p>Nemo enim ipsam voluptatem quia voluptas sit aspernatur aut odit aut qui ratione voluptatem sequi nesciunt. <b>READ MORE</b></p>
</article>

<footer class="abs footer">
  <div class="col" style="left:112px"><h4>Services</h4><ul><li>Emergency Room</li><li>Queries</li><li>Exams</li><li>Vaccines</li><li>Surgeries</li></ul></div>
  <div class="col" style="left:310px"><h4>Vita Pet</h4><ul><li>Units</li><li>Blog</li><li>Work with us</li><li>Who we are</li></ul></div>
  <div class="col" style="left:511px"><h4>Help</h4><ul><li>Ombudsman</li><li>Contact us</li></ul></div>
  <div class="col" style="left:705px"><h4>Tutors</h4><ul><li>Tutor area</li><li>Schedules</li><li>Examination results</li></ul></div>
  <div class="col" style="left:902px"><h4>Call Center</h4><ul><li>+55 21 2950-4417</li><li>Whatsapp</li><li>+55 21 97342-6150</li></ul></div>
  <div class="footer-rule"></div>
  <div class="social"><span></span><span></span><span></span><span></span></div>
  <div class="copyright">© COPYRIGHT 2021 VITA PET. ALL RIGHTS RESERVED</div>
</footer>

</body>
</html>
```